Recruiting ad for Caregivers and Nurses

We need a few amazing, fun, catchy, creative recruiting ads for Caregivers and Nurses to care for homecare patients on the island of Oahu, in Hawaii. We are an in home care company called Parkdale Homecare. Our care services are provided 24/7, so we need staff that can work days, nights, weekdays, weekends. We need catchy fun ads to entice caregivers and nurses to call our office to inquire about jobs available. Our patients age range is from babies to seniors. We need caregivers and nurses for basic patient care (bathing, dressing, ambulating, preparing meals, medication reminders, light housekeeping) and complex patients (oxygen, tube feeding, injections, vents, wound care). Here are some bullets to consider including:
*Full-time and Part-time Positions Available (days, nights, weekdays, weekends)
*Sign-On Bonus Programs Offered up to $500
*Refer a Friend Bonus Program
*Holiday Pay
*2 Health Plans to Choose from
*Island-Wide Locations
*All PPE Provided (masks, gloves, etc)
*401K Program
*Tuition Benefits

```html
<!DOCTYPE html>
<html lang="en">
<head>
<meta charset="utf-8">
<title>Parkdale Homecare – Caregiver Recruiting</title>
<link href="https://fonts.googleapis.com/css2?family=Archivo+Black&family=Montserrat:wght@500;600;700;800&family=Roboto+Condensed:wght@500;600&display=swap" rel="stylesheet">
<style>
  :root{
    --teal:#137566;
    --teal-dark:#0b3a36;
    --teal-line:#2e9a82;
    --mint:#3fbf9a;
    --salmon:#f4a183;
    --ink:#111111;
    --paper:#e9eaee;
    --white:#ffffff;
  }
  *{margin:0;padding:0;box-sizing:border-box}
  html,body{width:833px;height:1200px;overflow:hidden;background:var(--paper)}
  .flyer{position:relative;width:833px;height:1200px;background:var(--teal);overflow:hidden;font-family:'Montserrat',sans-serif;color:var(--white)}
  .hero{position:absolute;left:0;top:0;width:833px;height:488px;background:linear-gradient(90deg,#b9b3ab 0%,#d4d2d0 45%,#e4e5ea 70%,#dfe1e6 100%)}
  .hero-photo{position:absolute;left:0;top:0;width:450px;height:488px;background:radial-gradient(ellipse at 45% 45%,#8a5a3e 0%,#a97a5c 30%,#c9c3bb 62%,rgba(210,208,206,0) 80%)}
  .hero-rule{position:absolute;left:378px;top:200px;width:6px;height:288px;background:var(--teal)}
  .caption{position:absolute;left:96px;top:458px;font-family:'Roboto Condensed',sans-serif;font-size:11px;color:var(--white)}
  .headline{position:absolute;left:446px;top:112px;font-family:'Archivo Black',sans-serif;font-size:56px;line-height:61px;color:var(--ink);letter-spacing:-0.5px}
  .headline-bar{position:absolute;left:452px;top:434px;width:318px;height:21px;background:var(--teal)}
  .meet{position:absolute;left:58px;top:524px;font-size:39px;font-weight:800;letter-spacing:0.3px;white-space:nowrap}
  .cta-band{position:absolute;left:0;top:590px;width:833px;height:94px;background:var(--teal-dark)}
  .cta-band .heart{position:absolute;left:172px;top:18px}
  .cta-band .cta{position:absolute;left:272px;top:10px;font-size:50px;font-weight:700;letter-spacing:-0.5px}
  .curve-arrow{position:absolute}
  .positions{position:absolute;left:111px;top:704px;font-size:23.5px;font-weight:600;white-space:nowrap}
  .shifts{position:absolute;top:752px;left:0;width:833px;height:30px}
  .shift{position:absolute;top:0;display:flex;align-items:center;gap:14px;font-size:16px;font-weight:500}
  .divider{position:absolute;height:2px;background:var(--teal-line)}
  .refer{position:absolute;left:44px;top:827px;display:flex;align-items:center;gap:13px}
  .refer-text{font-family:'Roboto Condensed',sans-serif;font-weight:600;font-size:16px;line-height:19px}
  .ribbon{position:absolute;left:270px;top:816px}
  .bonus-text{position:absolute;left:327px;top:845px;font-family:'Roboto Condensed',sans-serif;font-weight:600;font-size:15px;white-space:nowrap}
  .bonus-text .hl{color:var(--mint)}
  .bonus-amount{position:absolute;left:639px;top:815px;width:76px;height:76px;border-radius:50%;background:var(--teal-dark);display:flex;align-items:center;justify-content:center;font-weight:700;font-size:21px}
  .bonus-amount small{font-size:12px;margin-right:1px}
  .perks{position:absolute;left:88px;list-style:none}
  .perks li{display:flex;align-items:center;gap:10px;height:31px;font-family:'Roboto Condensed',sans-serif;font-weight:600;font-size:17.5px}
  .k401{position:absolute;left:388px;top:906px;width:100px;height:100px;border-radius:50%;border:4px solid var(--salmon);overflow:hidden;text-align:center}
  .k401 .big{margin-top:18px;font-weight:800;font-size:22px;line-height:24px}
  .k401 .small{font-family:'Roboto Condensed',sans-serif;font-weight:600;font-size:15px;color:var(--salmon)}
  .k401 svg{position:absolute;left:0;bottom:0}
  .brand-panel{position:absolute;left:515px;top:921px;width:318px;height:279px;background:linear-gradient(90deg,#eef0f3 0%,#eceef1 45%,#d9d2cc 70%,#c9d3de 100%)}
  .brand{position:absolute;left:548px;top:1010px;display:flex;flex-direction:column;align-items:center;gap:6px}
  .brand-mark{width:30px;height:30px;background:var(--salmon)}
  .brand-name{font-weight:700;font-size:20px;color:var(--teal);line-height:23px;text-align:center}
  .apply{position:absolute;left:87px;top:1133px;font-size:25px;font-weight:600;white-space:nowrap}
  .apply .url{margin-left:24px;font-size:21px;font-weight:500}
</style>
</head>
<body>
<main class="flyer">
  <section class="hero">
    <div class="hero-photo" role="img" aria-label="Portrait photo of Makoa, a 95-year-old patient in a straw hat"></div>
    <div class="hero-rule"></div>
    <p class="caption">Makoa, 95 years old patient from Honolulu</p>
    <h1 class="headline">MAKOA<br>KNOWS<br>EVERY<br>HAWAIIAN<br>SONG.</h1>
    <div class="headline-bar"></div>
  </section>

  <h2 class="meet">MEET MAKOA AND MANY OTHERS</h2>

  <div class="cta-band">
    <svg class="heart" width="58" height="46" viewBox="0 0 58 46"><path d="M29 44 C14 30 4 22 4 13 C4 6 10 3 16 3 C23 3 27 8 29 13 C31 8 35 3 42 3 C48 3 54 6 54 13 C54 22 44 30 29 44" fill="none" stroke="#3fbf9a" stroke-width="5" stroke-linejoin="round"/></svg>
    <p class="cta">be our caregiver</p>
  </div>

  <svg class="curve-arrow" style="left:24px;top:584px" width="140" height="90" viewBox="0 0 140 90"><path d="M36 4 C8 20 0 60 50 80 C60 84 72 85 130 86" fill="none" stroke="#111" stroke-width="3"/><path d="M125 88 L134 86 L126 80" fill="none" stroke="#111" stroke-width="3"/></svg>

  <p class="positions">FULL-TIME and PART-TIME Positions Available</p>

  <div class="shifts">
    <div class="shift" style="left:186px">
      <svg width="26" height="26" viewBox="0 0 26 26"><circle cx="13" cy="13" r="6" fill="none" stroke="#f4a183" stroke-width="3"/><g stroke="#f4a183" stroke-width="3" stroke-linecap="round"><path d="M13 1v3M13 22v3M1 13h3M22 13h3M4.5 4.5l2 2M19.5 19.5l2 2M4.5 21.5l2-2M19.5 6.5l2-2"/></g></svg>
      <span>days</span>
    </div>
    <div class="shift" style="left:302px">
      <svg width="20" height="22" viewBox="0 0 20 22"><path d="M14 1 A10 10 0 1 0 19 17 A8 8 0 0 1 14 1Z" fill="#fff"/></svg>
      <span>nights</span>
    </div>
    <div class="shift" style="left:416px">
      <svg width="20" height="22" viewBox="0 0 20 22"><rect x="1" y="4" width="18" height="17" rx="2" fill="#3fbf9a"/><rect x="4" y="1" width="3" height="5" fill="#3fbf9a"/><rect x="13" y="1" width="3" height="5" fill="#3fbf9a"/><g fill="#137566"><rect x="4" y="10" width="3" height="3"/><rect x="9" y="10" width="3" height="3"/><rect x="14" y="10" width="3" height="3"/><rect x="4" y="15" width="3" height="3"/><rect x="9" y="15" width="3" height="3"/><rect x="14" y="15" width="3" height="3"/></g></svg>
      <span>weekdays</span>
    </div>
    <div class="shift" style="left:558px">
      <svg width="22" height="22" viewBox="0 0 22 22"><circle cx="11" cy="11" r="8" fill="none" stroke="#f4a183" stroke-width="5"/><g stroke="#fff" stroke-width="2"><path d="M5 5l3 3M17 5l-3 3M5 17l3-3M17 17l-3-3"/></g></svg>
      <span>weekends</span>
    </div>
  </div>

  <div class="divider" style="left:111px;top:802px;width:617px"></div>

  <div class="refer">
    <svg width="54" height="54" viewBox="0 0 54 54"><circle cx="27" cy="27" r="24" fill="none" stroke="#f4a183" stroke-width="3"/><rect x="13" y="16" width="28" height="21" rx="3" fill="#fff"/><circle cx="20" cy="24" r="3" fill="#137566"/><path d="M15 32 a5 4 0 0 1 10 0Z" fill="#137566"/><g stroke="#137566" stroke-width="2"><path d="M28 22h9M28 26h9M28 30h9"/></g></svg>
    <p class="refer-text">Refer a Friend<br>BONUS Program</p>
  </div>

  <svg class="ribbon" width="380" height="70" viewBox="0 0 380 70"><path d="M0 22 H370 V66 H0 Q16 44 0 22Z" fill="#0b3a36"/><path d="M130 22 A28 22 0 0 1 184 22" fill="none" stroke="#3fbf9a" stroke-width="3"/><path d="M26 28 V60 M298 28 V60" stroke="#3fbf9a" stroke-width="2" stroke-dasharray="2 3"/></svg>
  <p class="bonus-text">SIGN-ON <span class="hl">BONUS</span> Programs offered up to</p>
  <div class="bonus-amount"><small>$</small>500</div>

  <ul class="perks" style="top:909px">
    <li><svg width="20" height="20" viewBox="0 0 20 20"><circle cx="10" cy="10" r="8.5" fill="none" stroke="#3fbf9a" stroke-width="2"/><path d="M6 10l3 3 5-6" fill="none" stroke="#3fbf9a" stroke-width="2"/></svg>Holiday Pay</li>
    <li><svg width="20" height="20" viewBox="0 0 20 20"><circle cx="10" cy="10" r="8.5" fill="none" stroke="#3fbf9a" stroke-width="2"/><path d="M6 10l3 3 5-6" fill="none" stroke="#3fbf9a" stroke-width="2"/></svg>2 Health Plans to Choose from</li>
    <li><svg width="20" height="20" viewBox="0 0 20 20"><circle cx="10" cy="10" r="8.5" fill="none" stroke="#3fbf9a" stroke-width="2"/><path d="M6 10l3 3 5-6" fill="none" stroke="#3fbf9a" stroke-width="2"/></svg>Island-Wide Locations</li>
  </ul>
  <ul class="perks" style="top:1021px">
    <li><svg width="20" height="20" viewBox="0 0 20 20"><circle cx="10" cy="10" r="8.5" fill="none" stroke="#3fbf9a" stroke-width="2"/><path d="M6 10l3 3 5-6" fill="none" stroke="#3fbf9a" stroke-width="2"/></svg>All PPE Provided (masks, gloves, etc)</li>
    <li><svg width="20" height="20" viewBox="0 0 20 20"><circle cx="10" cy="10" r="8.5" fill="none" stroke="#3fbf9a" stroke-width="2"/><path d="M6 10l3 3 5-6" fill="none" stroke="#3fbf9a" stroke-width="2"/></svg>Tuition Benefits</li>
  </ul>

  <div class="k401">
    <p class="big">401K</p>
    <p class="small">Program</p>
    <svg width="92" height="26" viewBox="0 0 92 26"><path d="M0 10 Q23 0 46 10 T92 8 V26 H0Z" fill="#f4a183"/></svg>
  </div>

  <div class="brand-panel" role="img" aria-label="Photo of a smiling nurse in a white coat reading a clipboard"></div>
  <div class="brand">
    <div class="brand-mark"></div>
    <p class="brand-name">Parkdale<br>Homecare</p>
  </div>

  <div class="divider" style="left:29px;top:1115px;width:520px"></div>

  <svg class="curve-arrow" style="left:0;top:1128px" width="80" height="72" viewBox="0 0 80 72"><path d="M6 72 C2 40 20 20 66 14" fill="none" stroke="#111" stroke-width="3"/><path d="M58 6 L68 14 L58 22" fill="none" stroke="#111" stroke-width="3"/></svg>

  <p class="apply">APPLY at <span class="url">parkdalecare.com/jobs</span></p>
</main>
</body>
</html>
```